Jumbo Postcard for Pizza Restaurant

i have ordered several thousand postcards already. My postcard has my menu on the back and information about my restaurant on the front. I would like to redesign my existing postcard. The key points of the postcard redesign are as follows.
1. I want to keep the menu on the back but I need to add some menu items and would like the layout to be reformatted so it is easier to read and use. There are also some menu items/descriptions on existing postcard that are too small and don't match the rest of the menu format (specifically: Pastas and Salads)
2. I would like to change the front of the postcard by adding coupons/offers to the customers. I would also like to add new pictures. I will upload pictures and ideas for coupon/offer later this evening. If you wish to proceed before then, perhaps you could just use a space filler until files are received. The overall look of the front of the postcard needs to be changed to reflect the new information and items so our customers take notice it and try new products.
3. The post card needs to be attention-grabbing and new when contrasted and compared to the previous postcard, but I do want it to be clear that it's originating from the same company. Our logo and use of the colors red, black and white should provide some continuity. I am not opposed to adding more color.
4. Just to give you an idea of who we are: We are a family owned and operated restaurant. We offer high quality, fresh ingredients and a premium product for a fair price. We are primarily a delivery and pickup restaurant, but we also have a small dine-in area.
5. When viewing the old postcard (I have uploaded the file) you'll notice an offer to get a second pizza of equal or lesser value for $12. I would like to make this offer more noticeable.
Updates
Project Deadline Extended Reason: I want to extend the deadline for two reasons. 1. I recently had a computer failure that resulted in the loss of some content, including some elements that were to be included in the postcard. I believe I have retrieved the necessary items.2. I am a very busy small business owner and have struggled to find time to work on this postcard and also do everything else required in a day. I appreciate the work, creativity, and submissions of all designers. I am asking for understanding on this matter. It's truly appreciated. Added Tuesday, March 22, 2016
Project Deadline Extended Reason: Need to work out final details. Thanks. Added Friday, April 1, 2016
Target Market(s)
We target families and also have a business lunch crowd.
Industry/Entity Type
Restaurant
Look and feel
Each slider illustrates characteristics of the customer's brand and the style your logo design should communicate.

```html
<!DOCTYPE html>
<html lang="en">
<head>
<meta charset="utf-8">
<title>Harbor Point Pizza Company – Jumbo Postcard</title>
<link href="https://fonts.googleapis.com/css2?family=Cinzel:wght@500&family=Oswald:wght@500;700&family=Source+Sans+3:ital,wght@0,400;0,600;0,700;1,400&display=swap" rel="stylesheet">
<style>
  :root{
    --red:#e31b23; --red-dark:#a50d12; --gold:#f2c230; --yellow:#ffe600;
    --orange:#f9b233; --black:#111; --white:#fff; --bg:#a9aaad; --ink:#333;
    --photo-dark:#3a2216; --photo-mid:#7a3a1c;
  }
  *{box-sizing:border-box;margin:0;padding:0}
  html,body{width:1167px;height:1200px;overflow:hidden}
  body{background:var(--bg);font-family:"Source Sans 3",sans-serif;color:var(--ink);position:relative}
  .card{position:absolute;overflow:hidden}

  /* FRONT */
  .front{left:120px;top:90px;width:907px;height:492px}
  .front-photo{position:absolute;inset:0;background:radial-gradient(ellipse at 55% 60%,#a3552a 0%,#6b2e16 45%,#2a170e 100%)}
  .tagline-band{position:absolute;left:348px;top:29px;right:0;height:45px;background:rgba(40,20,12,.75);
    font-family:"Cinzel",serif;color:var(--gold);font-size:32px;line-height:45px;text-align:center;letter-spacing:.5px}
  .order-panel{position:absolute;left:38px;top:27px;width:306px;height:431px;background:var(--red);
    border:2px solid var(--gold);border-radius:10px;text-align:center;color:var(--white);font-family:"Oswald",sans-serif}
  .brand-box{position:absolute;left:7px;top:7px;width:288px;height:179px;background:var(--white);border-radius:8px}
  .brand-mark{display:flex;align-items:center;justify-content:center;gap:10px;margin-top:38px}
  .brand-dot{width:26px;height:26px;border-radius:50%;background:var(--red)}
  .brand-name{font-family:"Oswald",sans-serif;font-weight:700;color:var(--red);font-size:24px;line-height:1.05;text-align:left}
  .brand-url{position:absolute;left:0;right:0;bottom:8px;font-family:"Source Sans 3",sans-serif;font-weight:700;color:#333;font-size:15px;letter-spacing:.4px}
  .call{position:absolute;top:196px;left:0;right:0;font-size:29px;font-weight:700;line-height:1}
  .phone{position:absolute;top:229px;left:0;right:0;font-size:44px;font-weight:700;line-height:1}
  .service{position:absolute;top:284px;left:0;right:0;font-size:19px;font-weight:500;line-height:1.2}
  .hours{position:absolute;top:340px;left:0;right:0;font-size:17px;font-weight:500;line-height:1.15;color:var(--yellow)}
  .front-address{position:absolute;top:406px;left:0;right:0;font-size:14px;font-weight:500}
  .map-box{position:absolute;left:606px;top:90px;width:262px;height:212px;background:var(--black);border:2px solid var(--white)}
  .map-info{position:absolute;right:8px;top:8px;text-align:right;font-size:10.5px;line-height:1.3;color:var(--white)}
  .map-info strong{display:block;color:var(--red);font-size:13px;font-weight:600;margin-bottom:2px}

  /* BACK */
  .back{left:120px;top:606px;width:905px;height:494px;background:var(--white)}
  .col{position:absolute;top:17px;font-size:7px;line-height:1.28}
  .col-1{left:12px;width:186px}.col-2{left:214px;width:192px}.col-3{left:422px;width:210px;top:14px}.col-4{left:642px;width:246px}
  .section-head{background:linear-gradient(90deg,var(--red),var(--red-dark));color:var(--white);font-size:12px;font-weight:600;padding:1px 0 1px 6px;margin-bottom:4px}
  .price-row{display:flex;justify-content:space-between;font-size:8.5px;line-height:1.55;padding:0 4px 0 2px}
  .price-row span:first-child{flex:1;overflow:hidden;white-space:nowrap}
  .price-row span:first-child::after{content:" ........................................................"}
  .note{font-size:5.5px;margin:1px 0 5px 2px}
  .choose-head{background:var(--orange);font-family:"Oswald",sans-serif;font-style:italic;font-weight:500;font-size:10.5px;color:#222;padding:1px 0 1px 2px;border-radius:0 6px 6px 0;margin:4px 0}
  .opts{display:grid;grid-template-columns:repeat(3,auto);gap:1px 6px;padding:2px;font-size:7px}
  .opts.two{grid-template-columns:1fr 1fr}
  .opts span::before{content:"";display:inline-block;width:5px;height:5px;background:var(--red);margin-right:3px}
  .col p{margin:0 2px 4px;text-align:justify}
  .col b{font-weight:700}
  .promo-bar{background:var(--red-dark);color:var(--yellow);font-family:"Oswald",sans-serif;font-weight:700;font-size:9.5px;line-height:1.1;padding:2px 5px;margin-top:6px}
  .hl{color:var(--red);font-weight:700}
  .col-4 p .hl:first-child{font-weight:600}
  .photo-strip{position:absolute;left:12px;top:322px;width:630px;height:158px;background:var(--red)}
  .photo{position:absolute;top:8px;height:144px;width:149px}
  .ph-pizza{left:6px;background:linear-gradient(135deg,#8c5a2b,#c9913f 50%,#5a3a1d)}
  .ph-wings{left:162px;background:linear-gradient(135deg,#3a1e10,#b4461c 50%,#4a2412)}
  .ph-pasta{left:474px;background:linear-gradient(135deg,#5a1510,#a8382a 50%,#e0d2b5)}
  .coupon{position:absolute;left:318px;top:8px;width:150px;height:144px;background:var(--orange);border:1.5px dashed var(--red);padding:5px 7px}
  .coupon h3{font-family:"Oswald",sans-serif;font-weight:700;color:var(--white);font-size:16.5px;line-height:1.16}
  .coupon-foot{position:absolute;left:7px;bottom:6px;display:flex;align-items:center;gap:6px}
  .coupon-dot{width:28px;height:28px;border-radius:50%;background:var(--red)}
  .coupon ul{list-style:none;font-size:7.5px;color:var(--red-dark);font-weight:700;line-height:1.4}
  .coupon li::before{content:"";display:inline-block;width:5px;height:5px;background:var(--red);margin-right:3px}
  .return{position:absolute;left:655px;top:292px;display:flex;align-items:center;gap:10px;font-size:9px;line-height:1.3}
  .return-dot{width:44px;height:44px;border-radius:50%;background:var(--red);border:2px solid var(--white);box-shadow:0 0 0 1px var(--red)}
  .indicia{position:absolute;left:822px;top:290px;width:61px;height:46px;border:1px solid #333;text-align:center;font-size:5.5px;font-weight:700;line-height:1.15;padding-top:2px}
  .indicia .paid{font-size:10px}
  .mail-box{position:absolute;left:729px;top:374px;width:154px;height:58px;border:1px solid #333;font-size:7.5px;padding:5px 8px}
  .mail-box .code{text-align:center;margin-bottom:14px}
  .mail-box b{display:block;line-height:1.35}
</style>
</head>
<body>

<section class="card front">
  <div class="front-photo" role="img" aria-label="Close-up photograph of a loaded supreme pizza with sausage, olives, onions and a bowl of marinara sauce"></div>
  <div class="tagline-band">PIZZA - PASTA - WINGS - SALAD</div>

  <div class="order-panel">
    <div class="brand-box">
      <div class="brand-mark">
        <span class="brand-dot"></span>
        <span class="brand-name">Harbor Point<br>Pizza Company</span>
      </div>
      <div class="brand-url">www.harborpointpizzaco.com</div>
    </div>
    <div class="call">Call to ORDER</div>
    <div class="phone">808-555-0142</div>
    <div class="service">Offering Take-out and<br>Free Delivery in Central Maui</div>
    <div class="hours">Monday - Thursday:&nbsp; 11am to 9.30pm<br>Friday - Saturday:&nbsp; 11am to 10pm<br>Sunday:&nbsp; 11am to 8.30pm</div>
    <div class="front-address">48 Kelo Street, Kahului, HI 96732</div>
  </div>

  <div class="map-box" role="img" aria-label="Street map showing the restaurant location near the highway">
    <div class="map-info">
      <strong>Harbor Point Pizza Co.</strong>
      48 Kelo Street, Kahului<br>in Palm Grove Village Center<br>(Next to the Corner Gas Station)
    </div>
  </div>
</section>

<section class="card back">
  <div class="col col-1">
    <div class="section-head">Custom Pizzas</div>
    <div class="price-row"><span>14” Small 1 Topping</span><span>$17.49</span></div>
    <div class="price-row"><span>16” Medium 1 Topping</span><span>$19.49</span></div>
    <div class="price-row"><span>18” Large 1 Topping</span><span>$21.49</span></div>
    <div class="note">Mozzarella cheese is included in the price of all pizzas</div>
    <div class="choose-head">Choose Your Crust:</div>
    <div class="opts"><span>Classic Hand Tossed</span><span>Pan Crust</span><span>Thin Crust</span></div>
    <div class="choose-head">Choose Your Sauce:</div>
    <div class="opts two"><span>Classic Marinara</span><span>Pesto</span><span>Alfredo</span><span>Barbecue</span></div>
    <div class="choose-head">Toppings: 2.00 each</div>
    <p>MEATS: Pepperoni, Italian Sausage, Ham, Bacon, Chicken, Ground Beef, Salami</p>
    <p>CHEESE: Mozzarella, Swiss, Feta, Smoked Gouda, Parmesan, Goat Cheese, Blue Cheese</p>
    <p>VEGETABLES: Mushrooms, Maui Sweet Onions, Red Onions, Green Onions, Black Olives, Kalamata Olives, Green Peppers, Jalapenos (Fresh), Jalapenos (Pickled), Tomatoes, Pineapple, Fresh Garlic, Roasted Garlic, Artichoke Hearts, Roasted Peppers, Sundried Tomatoes, Fresh Cilantro</p>
    <div class="promo-bar">BUY ANY PIZZA AND RECEIVE A SECOND PIZZA<br>OF EQUAL OR LESSER VALUE FOR JUST $12!</div>
  </div>

  <div class="col col-2">
    <div class="section-head">Specialty Pizzas</div>
    <div class="price-row"><span>14” Small</span><span>$21.49</span></div>
    <div class="price-row"><span>16” Medium</span><span>$23.49</span></div>
    <div class="price-row"><span>18” Large</span><span>$25.49</span></div>
    <p style="margin-top:4px"><b>The Stromboli:</b> Pepperoni, Red Onions, Green Peppers, and Italian Sausage</p>
    <p><b>The Widowmaker:</b> Ham, Salami, Pepperoni, Italian Sausage, Seasoned Ground Beef and Black Olives</p>
    <p><b>The Great Combo:</b> A hefty offering of Italian Sausage, Ham, Pepperoni, Mushrooms, Red Onions, Green Peppers and Black Olives</p>
    <p><b>The Beach (veg.):</b> Mushrooms, Red Onions, Green Peppers, Black Olives and Fresh Tomatoes</p>
    <p><b>The Big Wave (veg.):</b> Sweet Roasted Garlic, Mushrooms, Goat Cheese, Onions, Roasted Peppers and Sun Dried Tomatoes</p>
    <p><b>The Bleu Bacon:</b> Bacon, Bleu Cheese Crumbles &amp; Green Onions</p>
    <p><b>The Barbeque Chicken:</b> Oven Roasted Chicken, Red Onions, Smoked Gouda Cheese, and Fresh Cilantro over Robust Barbeque Sauce</p>
    <p><b>The Chicken Pesto:</b> Grilled Chicken Tomatoes and Mushrooms over fresh Pesto Sauce</p>
    <p><b>The Grizzly Pesto:</b> Italian Sausage, Artichoke Hearts and Feta Cheese over fresh Pesto Sauce</p>
    <p><b>The Greek:</b> Salami, Kalamata Olives, Feta Cheese and Marinated Artichoke Hearts over fresh Pesto Sauce</p>
  </div>

  <div class="col col-3">
    <p><b>The Cordon Bleu:</b> Oven Roasted Chicken, Ham, Swiss Cheese, Bleu Cheese Crumbles &amp; Mushrooms over creamy Alfredo Sauce</p>
    <div class="section-head">Wings</div>
    <div class="price-row"><span>6 piece wings</span><span>$4.99</span></div>
    <div class="price-row"><span>12 piece wings</span><span>$8.99</span></div>
    <div class="price-row"><span>24 piece wings</span><span>$17.99</span></div>
    <p style="margin-top:3px"><b>Chicken Wings:</b> Cooked to crispy perfection! Wings are served with celery or carrot sticks and your choice of homemade dressing—ranch or bleu cheese. Choose hot, medium, mild or barbeque.</p>
    <div class="section-head">Cheese &amp; Garlic Bread</div>
    <p><b>Garlic Cheese Bread:</b> Fresh, homemade bread covered in real butter, garlic, oregano, parmesan and mozzarella cheese. 4 pc – $5.49 or 8 pc – $8.49</p>
    <p><b>Garlic Bread:</b> Fresh, homemade bread covered in real butter, garlic and oregano. 4pc – $3.49 or 8pc – $6.49</p>
    <p><b>Cheese Pull Apart:</b> Fresh pizza dough covered in butter &amp; garlic then topped with mozzarella, gouda and oregano. 10”- $8.49</p>
    <div class="section-head">Sandwiches</div>
    <p><b>Meatball Sub:</b> Homemade meatballs on a fresh baked bread, served with marinara sauce and your choice of cheese. $10.99</p>
    <div class="promo-bar" style="text-align:center;margin-top:3px">CALL TO FIND OUT ABOUT OUR NEW<br>SANDWICH MENU! &nbsp; 808-555-0142</div>
  </div>

  <div class="col col-4">
    <div class="section-head">Desserts &amp; Beverages</div>
    <p><span class="hl">DESSERTS:</span> <b>Fresh Baked Cookies:</b> Soft, chewy, and delicious! Chocolate Chip, Oatmeal, or Peanut Butter.<br>Single cookie- $0.75, Half dozen- $3.99, One dozen $7.49</p>
    <p><span class="hl">ICE CREAM:</span> <b>Creamery Lane Ice Cream</b> (call for available flavors) One Pint - $5.99</p>
    <p><span class="hl">BEVERAGES:</span> Cola, Diet Cola, Cherry Pop, Zero Cola, Lemon-Lime, Root Beer. <i>12 oz. can - $1.50 each, 6 Pack- $3.50, 12 Pack-$6.00</i></p>
    <div class="section-head">Salads &amp; Pasta</div>
    <p><span class="hl">Garden Salad-</span> Iceberg Lettuce, Kula Cabbage, Black Olives, Cucumbers, Tomatoes. <i>Served with homemade croutons and choice of dressing.</i> <span class="hl">$8.49</span></p>
    <p><span class="hl">Chef Salad:</span> Iceberg Lettuce, Kula Cabbage, Black Olives, Green Onions, Tomatoes, Bacon, Grilled Chicken, Mozzarella Cheese. <i>Served with homemade croutons and choice of dressing.</i> <span class="hl">$10.49</span><br>Dressing ~ Ranch, Bleu Cheese or Balsamic Vinaigrette</p>
    <p><span class="hl">PASTA: Spaghetti with Meat Sauce-</span> Served with garlic bread and a side of parmesan cheese $9.49</p>
    <p><span class="hl">PASTA: Spaghetti with Marinara Sauce:</span> Served with garlic bread and a side of parmesan cheese $8.49</p>
  </div>

  <div class="photo-strip">
    <div class="photo ph-pizza" role="img" aria-label="Photograph of a pesto pizza with tomatoes and mushrooms"></div>
    <div class="photo ph-wings" role="img" aria-label="Photograph of spicy chicken wings with dipping sauce"></div>
    <div class="coupon">
      <h3>One FREE 4 PIECE CHEESE BREAD with the purchase of any Medium or Large pizza</h3>
      <div class="coupon-foot">
        <span class="coupon-dot"></span>
        <ul><li>Coupon required</li><li>Limit one per order</li><li>Expires 08/31/16</li></ul>
      </div>
    </div>
    <div class="photo ph-pasta" role="img" aria-label="Photograph of spaghetti with meat sauce and parmesan"></div>
  </div>

  <div class="return">
    <span class="return-dot"></span>
    <span>48 Kelo Street,<br>Kahului, HI 96732</span>
  </div>
  <div class="indicia">PRSRT STD<br>ECRWSS<br>U.S.POSTAGE<br><span class="paid">PAID</span><br>EDDM Retail</div>
  <div class="mail-box">
    <div class="code">****************ECRWSS****</div>
    <b>Local</b><b>Postal Customer</b>
  </div>
</section>

</body>
</html>
```